Massage Therapy Business Card

I’d like the same exact business card (same graphics and colors) that I uploaded by R & K Designer with:
Name of the business: Bodywork by Delmar;
Delmar Hollis (Massage Therapist);
Contact: (555)-418-2073
Email: bodyworkbydelmar@quillmail.test;
IG: @Gr4in_bodywork

On the back Please add:
1. Mobile Sessions available upon request
2. Book 3 Massages, Get 4th 50% off

Target Market(s)

Adults ages 21+

Industry/Entity Type

Healthcare and Therapy

Contact Information for Business Card

The color should be different shades of blue with a logo of a male anatomy and pressure points for massages

Colors
0054AA
0677BA
7BADD7
CADEEF
E8F1F8
0094D4
00A9DD
6FCCEA
C7EBF8
E9F6FB
00AB8E
00BBA5
67D7C9
C6EFE9
E9F9F6
EB3D1F
EC4F4E
F09395
F8D3D4
FCEDEE

Requirements
Must have
• Must be Double Sided
Nice to have
• Newer Modern look with a Masculine Feel

```html
<!DOCTYPE html>
<html lang="en">
<head>
<meta charset="utf-8">
<title>Bodywork by Delmar – Business Card</title>
<link rel="stylesheet" href="https://fonts.googleapis.com/css2?family=Poppins:wght@400;600&family=Roboto:wght@400;700&display=swap">
<style>
  :root {
    --page-bg: #ececec;
    --header-bg: #ffffff;
    --title-blue: #2a66ad;
    --card-top: #2a7dc2;
    --card-bottom: #2155a8;
    --figure-dark: #0f2f7a;
    --figure-glow: #3d8ee0;
    --pain-red: #eb3d1f;
    --pain-pink: #f09395;
    --ink-light: #ffffff;
    --badge: #e9f1f8;
  }
  * { box-sizing: border-box; margin: 0; padding: 0; }
  html, body { width: 1200px; height: 1150px; overflow: hidden; }
  body { background: var(--page-bg); font-family: "Poppins", sans-serif; position: relative; }

  .presentation-header {
    position: absolute; top: 0; left: 0; width: 1200px; height: 157px;
    background: var(--header-bg); padding: 30px 0 0 68px;
    font-family: "Roboto", sans-serif; color: var(--title-blue);
  }
  .presentation-header h1 { font-size: 46px; font-weight: 700; line-height: 1.1; }
  .presentation-header p { font-size: 46px; font-weight: 400; line-height: 1.1; }

  .card {
    position: absolute; width: 680px; height: 390px; border-radius: 30px; overflow: hidden;
    background: linear-gradient(160deg, var(--card-top), var(--card-bottom));
    box-shadow: 0 14px 28px rgba(0,0,0,0.22);
    color: var(--ink-light);
  }
  .card--back { left: 50px; top: 200px; }
  .card--front { left: 470px; top: 720px; }

  .card__figure { position: absolute; }
  .card--back .card__figure {
    left: 40px; top: 0; width: 300px; height: 390px;
    background: radial-gradient(ellipse at 55% 45%, var(--pain-red) 0%, var(--figure-glow) 22%, var(--figure-dark) 55%, transparent 78%);
  }
  .card--front .card__figure {
    left: 40px; top: 30px; width: 260px; height: 340px;
    background: radial-gradient(ellipse at 45% 55%, var(--pain-pink) 0%, var(--figure-glow) 30%, rgba(15,47,122,0.5) 60%, transparent 80%);
  }

  .offers { position: absolute; left: 330px; top: 70px; list-style: none; }
  .offers li { display: flex; align-items: center; gap: 10px; font-size: 17px; margin-bottom: 12px; }
  .offers strong { font-weight: 600; }
  .offers svg { width: 22px; height: 22px; flex: none; }

  .brand { position: absolute; display: flex; align-items: center; gap: 14px; }
  .card--back .brand { left: 330px; top: 215px; }
  .card--front .brand { left: 320px; top: 40px; }
  .brand__mark { width: 62px; height: 62px; border-radius: 50%; background: var(--badge); flex: none; }
  .brand__name { font-size: 21px; font-weight: 400; letter-spacing: 0.5px; line-height: 1.1; }
  .brand__tag { font-size: 14px; }

  .person { position: absolute; left: 330px; top: 150px; }
  .person__name { font-size: 25px; font-weight: 600; line-height: 1.15; }
  .person__role { font-size: 16px; }

  .contact { position: absolute; left: 330px; top: 230px; list-style: none; }
  .contact li { display: flex; align-items: center; gap: 12px; font-size: 16px; margin-bottom: 10px; }
  .contact svg { width: 20px; height: 20px; flex: none; }
</style>
</head>
<body>
  <header class="presentation-header">
    <h1>Business Card - Mockup 1</h1>
    <p>Rounded Edge</p>
  </header>

  <section class="card card--back">
    <div class="card__figure" role="img" aria-label="Glowing male anatomy figure holding neck and lower back, spine highlighted with red pressure points"></div>
    <ul class="offers">
      <li><svg viewBox="0 0 24 24"><path d="M12 0 L14 10 L24 12 L14 14 L12 24 L10 14 L0 12 L10 10 Z" fill="#fff"/></svg>Mobile Sessions available upon request</li>
      <li><svg viewBox="0 0 24 24"><path d="M12 0 L14 10 L24 12 L14 14 L12 24 L10 14 L0 12 L10 10 Z" fill="#fff"/></svg>Book 3 Massages,&nbsp;<strong>Get 4th 50% off</strong></li>
    </ul>
    <div class="brand">
      <span class="brand__mark"></span>
      <div>
        <div class="brand__name">BODYWORK BY DELMAR</div>
        <div class="brand__tag">Massage Therapy Centre</div>
      </div>
    </div>
  </section>

  <section class="card card--front">
    <div class="card__figure" role="img" aria-label="Translucent blue skeleton figure bending over with glowing pink pressure points on hip, knee and ankle"></div>
    <div class="brand">
      <span class="brand__mark"></span>
      <div>
        <div class="brand__name">BODYWORK BY DELMAR</div>
        <div class="brand__tag">Massage Therapy Centre</div>
      </div>
    </div>
    <div class="person">
      <div class="person__name">Delmar Hollis</div>
      <div class="person__role">Massage Therapist</div>
    </div>
    <ul class="contact">
      <li><svg viewBox="0 0 24 24"><rect x="6" y="2" width="12" height="20" rx="2" fill="none" stroke="#fff" stroke-width="2"/></svg>(555)-418-2073</li>
      <li><svg viewBox="0 0 24 24"><rect x="2" y="5" width="20" height="14" rx="1" fill="none" stroke="#fff" stroke-width="2"/><path d="M2 6 L12 13 L22 6" fill="none" stroke="#fff" stroke-width="2"/></svg>bodyworkbydelmar@quillmail.test</li>
      <li><svg viewBox="0 0 24 24"><rect x="4" y="4" width="16" height="16" fill="#fff"/></svg>@Gr4in_bodywork</li>
    </ul>
  </section>
</body>
</html>
```